Security camera surveillance warning Sign

Security Camera Sign 11" x 11" Red, Yellow and Black (White Background)
I would like a line drawing of camera image attached.
Wording: All Suspicious or Criminal Activity Will Be Reported!
WARNING
24 HOUR SURVEILLANCE

Industry/Entity Type

Security

Colors
ec1f27
000000
ffc214

Requirements
Nice to have
• I uploaded a sign and would like the new design look something like that

```html
<!DOCTYPE html>
<html lang="en">
<head>
<meta charset="utf-8">
<title>24 Hour Surveillance Sign</title>
<link rel="stylesheet" href="https://fonts.googleapis.com/css2?family=PT+Sans:wght@400;700&display=swap">
<style>
  :root {
    --sign-red: #d42213;
    --sign-yellow: #f7df0f;
    --sign-black: #000000;
    --page-white: #ffffff;
    --label-grey: #c8c8c8;
    --art-tone: #e8cf0c;
  }
  html, body {
    margin: 0;
    padding: 0;
    overflow: hidden;
  }
  .canvas {
    position: relative;
    width: 1200px;
    height: 801px;
    background: var(--page-white);
    overflow: hidden;
    font-family: "PT Sans", Tahoma, sans-serif;
  }
  .sign {
    position: absolute;
    left: 324px;
    top: 125px;
    width: 552px;
    height: 551px;
  }
  .sign-header {
    height: 97px;
    background: var(--sign-red);
    color: var(--sign-yellow);
    display: flex;
    align-items: center;
    justify-content: center;
    font-weight: 700;
    font-size: 44px;
    letter-spacing: 0.5px;
  }
  .sign-body {
    position: relative;
    height: 322px;
    background: var(--sign-yellow);
  }
  .camera-art {
    position: absolute;
    left: 74px;
    top: 25px;
    width: 402px;
    height: 278px;
  }
  .sign-footer {
    height: 132px;
    background: var(--sign-black);
    color: var(--sign-yellow);
    display: flex;
    flex-direction: column;
    align-items: center;
    justify-content: center;
    font-weight: 700;
    font-size: 36px;
    line-height: 42px;
    text-align: center;
  }
  .size-label {
    position: absolute;
    right: 23px;
    top: 735px;
    color: var(--label-grey);
    font-weight: 700;
    font-size: 38px;
    letter-spacing: -1px;
    word-spacing: 8px;
  }
</style>
</head>
<body>
  <div class="canvas">
    <div class="sign">
      <div class="sign-header">24 HOUR SURVEILLANCE</div>
      <div class="sign-body">
        <svg class="camera-art" viewBox="0 0 402 278" role="img" aria-label="Line drawing of a wall-mounted CCTV security camera on a bracket">
          <rect x="0" y="0" width="402" height="278" rx="18" fill="var(--art-tone)"/>
        </svg>
      </div>
      <div class="sign-footer">
        <span>All Suspicious or Criminal</span>
        <span>Activity Will Be Reported!</span>
      </div>
    </div>
    <div class="size-label">Size: 11" x 11"</div>
  </div>
</body>
</html>
```